Visitenkarte erstellen für Reiki Praxis

Visitenkarten für Reiki Praxis Doppelseitig

business cards reiki practice double-sided

The background can also be a different color

```html
<!DOCTYPE html>
<html lang="en">
<head>
<meta charset="utf-8">
<title>Lumen Balance – Business Cards</title>
<link href="https://fonts.googleapis.com/css2?family=Roboto:wght@400;500;700&display=swap" rel="stylesheet">
<style>
  :root {
    --stage: #b5b5b0;
    --paper: #ffffff;
    --gold: #d9a224;
    --gold-deep: #cf9a2a;
    --rose: #b06a66;
    --magenta: #a14a74;
    --ink-light: #ffffff;
  }
  * { margin: 0; padding: 0; box-sizing: border-box; }
  html, body {
    width: 1200px; height: 810px; overflow: hidden;
    background: var(--stage);
    font-family: "Roboto", Arial, sans-serif;
  }
  .stage {
    position: relative; width: 1200px; height: 810px;
    display: flex; align-items: center; justify-content: center; gap: 40px;
  }
  .card {
    position: relative; width: 540px; height: 309px;
    box-shadow: 0 10px 28px rgba(0,0,0,.25);
    overflow: hidden;
  }

  /* Front: details side */
  .card--front { background: var(--paper); }
  .brand {
    position: absolute; left: 0; top: 0; width: 308px; height: 100%;
    display: flex; flex-direction: column; align-items: center; justify-content: center;
    color: var(--gold); font-weight: 500; text-align: center;
  }
  .brand__name { font-size: 24px; letter-spacing: 1.5px; }
  .brand__owner { font-size: 15px; letter-spacing: 6px; margin-top: 4px; }
  .divider {
    position: absolute; left: 308px; top: 44px; width: 2px; height: 218px;
    background: var(--gold);
  }
  .details {
    position: absolute; left: 330px; top: 54px; right: 20px;
    color: var(--gold);
  }
  .details__name { font-size: 22px; font-weight: 700; letter-spacing: .5px; line-height: 1; }
  .details__role { font-size: 11px; letter-spacing: .8px; margin-top: 4px; }
  .details__address { font-size: 12px; line-height: 1.35; margin-top: 26px; }
  .contact-list { list-style: none; margin-top: 14px; }
  .contact-list li {
    display: flex; align-items: center; gap: 9px;
    font-size: 12px; line-height: 1; margin-bottom: 10px;
  }
  .contact-list svg { width: 15px; height: 15px; flex: none; }

  /* Back: brand side */
  .card--back {
    background: linear-gradient(160deg, var(--gold-deep) 0%, var(--rose) 50%, var(--magenta) 100%);
  }
  .card--back .brand {
    width: 100%; color: var(--ink-light); font-weight: 400;
  }
  .card--back .brand__name { font-size: 34px; letter-spacing: 2px; }
  .card--back .brand__owner { font-size: 20px; letter-spacing: 9px; margin-top: 6px; }
</style>
</head>
<body>
<main class="stage">
  <section class="card card--front" aria-label="Business card front">
    <div class="brand">
      <span class="brand__name">LUMEN BALANCE</span>
      <span class="brand__owner">MARA KESSEL</span>
    </div>
    <div class="divider"></div>
    <div class="details">
      <p class="details__name">OWEN HARTLEY</p>
      <p class="details__role">GANERAL MANAGER</p>
      <p class="details__address">2750 Alder Lane, Ridgefield,<br>CA 91804</p>
      <ul class="contact-list">
        <li>
          <svg viewBox="0 0 16 16" fill="var(--gold)" aria-hidden="true"><path d="M3.5 1.5l2.3 2.6-1.2 1.6c.8 1.9 2.1 3.2 4 4l1.6-1.2 2.6 2.3-1.3 2.2C6.9 13.2 2.8 9.1 1.2 2.8z"/></svg>
          555-014-2298
        </li>
        <li>
          <svg viewBox="0 0 16 16" fill="none" stroke="var(--gold)" stroke-width="1.6" aria-hidden="true"><rect x="1.5" y="3.5" width="13" height="9"/><path d="M1.5 3.5L8 9l6.5-5.5"/></svg>
          hello@lumenbalance.com
        </li>
        <li>
          <svg viewBox="0 0 16 16" fill="none" stroke="var(--gold)" stroke-width="1.4" aria-hidden="true"><circle cx="8" cy="8" r="6.5"/><ellipse cx="8" cy="8" rx="3" ry="6.5"/><path d="M1.5 8h13M2.5 4.8h11M2.5 11.2h11"/></svg>
          www.lumenbalance.com
        </li>
      </ul>
    </div>
  </section>

  <section class="card card--back" aria-label="Business card back">
    <div class="brand">
      <span class="brand__name">LUMEN BALANCE</span>
      <span class="brand__owner">MARA KESSEL</span>
    </div>
  </section>
</main>
</body>
</html>
```